PSD Only - Wordpress Magazine Theme Design

We need a design for our new Premuim wordpress Magazine theme design based on our basic wire-frame. The theme will be used by people who run online magazine, news website or just blog in general.

The layout of homepage is showing recent posts in many way which is easy to user to customize the section of their homepage to show their post based on various categories.

2 Page design need (Homepage and Single Post)
Updates

Project Deadline Extended
Reason: want to get more designer and I am off for holiday a few days too. Better extend the time for designers as well as me also.

Target Market(s)

General Blogger who want a nice premium theme as well as other content based wesite.

Industry/Entity Type

Online

Font styles to use
Sans Serif

Requirements
Must have
• + Must have 2 page design based on Wireframing. Homepage (home.png) annd Single Post (Single.png)
• + Layout must be based on wireframe.
• + Width 1025px
• + 2 Navigation Menu in Header Must be in different style. When theme goes public, user can choose to have both or only 1 navigation or completely hide both of them.
• + 2 Featured Content Slider as you see in wire-frame. They must be in different style from each other.
• + Those recent news section is only about arrange post in defferent ways which only include post feature image, post title as well as post meta info.
• + Sidebar Widget Must be 300px (not include margin or padding) in order to be able for user to place ads with (300px of width) in sidebar widget)
• + Footer Widget Section should have a bit different colour in order to look different for main layout.
Nice to have
• + Drop down Menu
• + (Optional) Some custom Widget (Based on your imagination and creativity)

```html
<!DOCTYPE html>
<html lang="en">
<head>
<meta charset="utf-8">
<title>Magazine Theme – Homepage</title>
<link href="https://fonts.googleapis.com/css2?family=Open+Sans:ital,wght@0,400;0,600;0,700;1,400&display=swap" rel="stylesheet">
<style>
:root{
  --bg:#e8e8e8;
  --white:#ffffff;
  --dark:#333333;
  --darker:#262626;
  --nav:#3a3a3a;
  --widget:#3b3b3b;
  --blue:#3d5a9e;
  --blue-dark:#2c4580;
  --thumb:#777777;
  --text:#333333;
  --muted:#8a8a8a;
  --line:#d9d9d9;
  --red:#d9534f;
}
*{box-sizing:border-box;margin:0;padding:0}
html,body{width:1200px;height:3199px;overflow:hidden;background:var(--bg);font-family:"Open Sans",Arial,sans-serif;color:var(--text)}
.page{position:relative;width:1200px;height:3199px;overflow:hidden}
.abs{position:absolute}
ul{list-style:none}

/* top bar */
.topbar{left:75px;top:0;width:1050px;height:40px;background:var(--dark);display:flex;align-items:center;padding-left:16px}
.topbar a{color:#ddd;font-size:10px;margin-right:26px;text-decoration:none}
.topbar .social{margin-left:auto;display:flex;gap:8px;align-items:center;margin-right:10px}
.topbar .social span{width:11px;height:11px;background:#bbb;border-radius:2px}
.topbar .search-btn{width:30px;height:40px;background:var(--blue);display:flex;align-items:center;justify-content:center}

/* header */
.header{left:75px;top:40px;width:1050px;height:119px;background:var(--white)}
.logo{position:absolute;left:31px;top:22px}
.logo .name{font-size:44px;font-weight:700;color:var(--blue);line-height:1;letter-spacing:-1px}
.logo .slogan{font-size:14px;letter-spacing:2.5px;color:#333;margin-top:6px}
.ad{background:#000;color:#fff;font-size:13px;display:flex;align-items:center;justify-content:center}
.header .ad{position:absolute;left:342px;top:20px;width:682px;height:81px}

/* main nav */
.mainnav{left:75px;top:159px;width:1050px;height:44px;background:var(--nav);display:flex;align-items:center;padding-left:8px}
.mainnav a{color:#ddd;font-size:10px;padding:0 14px;height:44px;line-height:44px;text-decoration:none}
.mainnav a.active{background:#1f1f1f;color:#fff;font-weight:700}
.mainnav a.open{background:#454545}
.mainnav .search{margin-left:auto;margin-right:16px;width:194px;height:24px;background:#2b2b2b;border:1px solid #4a4a4a;color:#777;font-size:9px;padding-left:8px;line-height:22px}
.dropdown{left:384px;top:203px;width:190px;height:106px;background:var(--blue);padding:6px 8px;z-index:3}
.dropdown li{font-size:8px;color:#fff;height:31px;line-height:31px;padding-left:8px;text-transform:uppercase}
.dropdown li.current{background:var(--blue-dark)}

/* content area */
.content{left:75px;top:203px;width:1050px;height:2630px;background:var(--white)}

/* sliders */
.slider-main{left:88px;top:212px;width:1024px;height:395px;overflow:hidden}
.scene{width:100%;height:100%;background:radial-gradient(ellipse at 22% 25%,#c8506a 0%,#6b2a56 25%,#2d2440 55%,#1b2234 100%)}
.arrow{position:absolute;width:18px;height:18px}
.dots{position:absolute;display:flex;gap:5px}
.dots i{width:6px;height:6px;border-radius:50%;background:#888}
.dots i.on{background:#fff}
.caption{position:absolute;left:0;bottom:0;width:100%;height:76px;background:rgba(20,20,30,.55);padding:12px 20px}
.caption h2{font-size:18px;font-weight:400;color:#fff}
.caption p{font-size:13px;color:#888;line-height:17px;margin-top:6px}

.slider-second{left:88px;top:618px;width:682px;height:333px;overflow:hidden}
.slider-second .panel{position:absolute;left:0;top:0;width:349px;height:333px;background:linear-gradient(90deg,#2c2c30,#3a3038);padding:40px 40px 0 70px}
.slider-second .photo{position:absolute;left:349px;top:0;width:333px;height:333px;background:linear-gradient(160deg,#6d3d68 0%,#3b2b4c 45%,#1c2336 100%)}
.panel h2{font-size:21px;line-height:33px;font-weight:400;color:#fff}
.panel .time{font-size:14px;color:#fff;margin-top:10px}
.panel p{font-size:12px;color:#777;line-height:18px;margin-top:36px}
.panel .more{font-size:12px;color:var(--red);margin-top:10px}

/* section titles */
.section-title{font-size:23px;color:#333;font-weight:400}
.title-dots{display:flex;gap:5px}
.title-dots i{width:7px;height:7px;border-radius:50%;background:#333}
.title-dots i.on{background:var(--blue)}

/* thumbs */
.thumb{position:relative;background:var(--thumb);overflow:hidden}
.ribbon{position:absolute;left:0;top:0;background:var(--blue);clip-path:polygon(0 0,100% 0,0 100%)}
.ribbon span{position:absolute;color:#fff;transform:rotate(-45deg);transform-origin:center}

.post-icon{display:inline-flex;width:18px;height:18px;background:var(--blue);align-items:center;justify-content:center;flex:none}
.post-icon i{width:7px;height:9px;border:1.5px solid #fff}

.meta{display:flex;align-items:center;color:var(--muted)}
.meta svg{fill:var(--blue);flex:none}

/* grid cards */
.card{width:159px}
.card .thumb{height:140px}
.card .ribbon{width:40px;height:40px}
.card .ribbon span{left:0;top:8px;font-size:9px}
.card h3{display:flex;align-items:center;gap:6px;font-size:10px;font-weight:400;margin-top:14px}
.card h3 .post-icon{width:16px;height:16px}
.card p{font-size:9.5px;line-height:13px;margin-top:12px;color:#444}
.card .meta{font-size:6.5px;gap:4px;margin-top:14px}

/* two columns */
.col{width:330px}
.col .thumb{height:287px}
.col .ribbon{width:102px;height:102px}
.col .ribbon span{left:12px;top:22px;font-size:20px}
.col h3{display:flex;align-items:center;gap:10px;font-size:23px;font-weight:400;margin-top:13px}
.col h3 .post-icon{width:38px;height:38px}
.col h3 .post-icon i{width:12px;height:15px;border-width:2px}
.col p{font-size:20px;line-height:29px;margin-top:14px;color:#333}
.col .meta{font-size:11px;gap:8px;margin-top:14px}

/* list posts */
.wide{width:680px}
.wide .thumb{height:210px}
.wide .ribbon{width:102px;height:102px}
.wide .ribbon span{left:12px;top:22px;font-size:20px}
.wide h3{display:flex;align-items:center;gap:18px;font-size:19px;font-weight:400;margin-top:24px}
.wide h3 .post-icon{width:34px;height:34px}
.wide h3 .post-icon i{width:11px;height:14px;border-width:2px}
.wide p{font-size:12.5px;line-height:22px;margin-top:14px;padding-left:52px;color:#333}
.wide p a{color:var(--blue);text-decoration:none}
.wide .meta{font-size:13px;gap:12px;margin-top:14px;padding-left:52px}
.wide .meta span{margin-right:24px}

.pager{left:88px;top:2782px;width:680px;height:24px;background:var(--blue);display:flex;align-items:center;padding:0 8px;color:#fff;font-size:10px;font-weight:600}
.pager .num{width:30px;text-align:center;line-height:24px}
.pager .num.on{background:#1c2f5e}
.pager .newer{margin-left:auto}

/* sidebar */
.widget{left:779px;width:333px;background:var(--widget);color:#fff}
.widget-head{display:flex;align-items:center;justify-content:space-between;height:46px;padding:0 16px;border-bottom:1px solid #4b4b4b;font-size:15px}
.widget-head .title-dots i{width:6px;height:6px;background:#999}
.widget-head .title-dots i.on{background:#fff}
.signin{top:618px;height:123px;text-align:center;padding-top:12px}
.signin h4{font-size:17px;font-weight:400}
.signin p{font-size:9px;margin-top:6px;color:#ddd}
.signin .nets{display:flex;justify-content:center;gap:19px;margin-top:17px}
.signin .nets span{width:26px;height:26px;border-radius:50%}
.postlist{padding:16px 14px 0}
.postlist li{display:flex;gap:14px;height:86px}
.postlist .sq{width:72px;height:70px;background:var(--thumb);flex:none}
.postlist b{display:block;font-size:10.5px;line-height:17px;font-weight:600;margin-top:6px}
.postlist small{display:block;font-size:9px;color:#aaa;margin-top:6px}
.recent{top:754px;height:488px}
.popular{top:1853px;height:479px}
.newsletter{top:1257px;height:115px;text-align:center;padding-top:12px}
.newsletter h4{font-size:18px;font-weight:400}
.newsletter p{font-size:9px;color:#ddd;margin-top:3px}
.newsletter form{display:flex;justify-content:center;gap:10px;margin-top:16px}
.newsletter .field{width:210px;height:28px;background:#555;border:1px solid #777;font-size:10px;color:#bbb;text-align:left;padding-left:10px;line-height:26px}
.newsletter .btn{width:72px;height:28px;background:var(--blue);font-size:9px;font-weight:700;line-height:28px}
.category{left:779px;top:1392px;width:333px}
.category h4{font-size:13px;font-weight:400}
.tags{display:flex;flex-wrap:wrap;gap:5px 5px;margin-top:10px}
.tags span{background:#e4e4e4;border:1px solid #d2d2d2;font-size:9px;color:#555;padding:5px 10px}
.side-ad{left:779px;top:1555px;width:333px;height:276px}

/* footer */
.footer{left:75px;top:2833px;width:1050px;height:322px;background:var(--dark);color:#fff}
.footbar{left:75px;top:3155px;width:1050px;height:44px;background:var(--darker);color:#666;font-size:12px;display:flex;align-items:center;padding:0 20px}
.footbar .follow{margin-left:auto;display:flex;gap:9px;align-items:center}
.footbar .follow span{width:11px;height:11px;background:#999;border-radius:2px}
.flogo{left:31px;top:28px;width:300px}
.flogo .name{font-size:44px;font-weight:700;color:var(--blue);line-height:1;letter-spacing:-1px}
.flogo .slogan{font-size:14px;letter-spacing:2.5px;margin-top:6px}
.flogo p{font-style:italic;font-size:12.5px;line-height:20px;color:#bbb;margin-top:22px}
.fcol-title{font-size:20px;font-weight:400}
.tweets{left:388px;top:26px;width:295px}
.tweets li{display:flex;gap:14px;border-bottom:1px solid #555;padding:12px 0 6px;height:76px}
.tweets li:first-child{margin-top:14px}
.tweets .dot{width:22px;height:22px;border-radius:50%;background:#ccc;flex:none;margin-top:6px}
.tweets p{font-size:9.5px;line-height:14px}
.tweets small{display:block;text-align:right;font-size:8px;color:#999}
.calendar{left:741px;top:26px;width:243px}
.cal{margin-top:14px;background:#2b2b2b;padding:8px}
.cal .month{background:#222;height:24px;display:flex;align-items:center;justify-content:space-between;padding:0 8px;font-size:10px;font-weight:700}
.cal table{width:100%;border-collapse:collapse;margin-top:8px}
.cal td,.cal th{text-align:center;font-size:11px;font-weight:700;height:33px}
.cal th{height:22px}
.cal .o{color:#6c7fb0}
.cal .today span{display:inline-block;width:26px;height:24px;line-height:24px;background:#fff;color:#333}
</style>
</head>
<body>
<div class="page">

  <!-- top bar -->
  <div class="abs topbar">
    <a>Home</a><a>About Us</a><a>Contact Us</a><a>Resources</a>
    <div class="social"><span></span><span></span><span></span><span></span><span></span><span></span><span></span><span></span><span></span><span></span><span></span></div>
    <div class="search-btn"><svg width="13" height="13" viewBox="0 0 13 13"><circle cx="5.5" cy="5.5" r="4" fill="none" stroke="#fff" stroke-width="1.8"/><line x1="8.5" y1="8.5" x2="12" y2="12" stroke="#fff" stroke-width="1.8"/></svg></div>
  </div>

  <!-- header -->
  <div class="abs header">
    <div class="logo"><div class="name">Logo Here</div><div class="slogan">Logo Slogan Goes Here</div></div>
    <div class="ad">ADS</div>
  </div>

  <div class="abs content"></div>

  <!-- main navigation -->
  <nav class="abs mainnav">
    <a class="active">Home</a><a>Navigation 1</a><a>Navigation 2</a><a>Navigation 3</a><a class="open">Navigation 4</a><a>Navigation 5</a><a>Navigation 6</a>
    <div class="search">Search</div>
  </nav>
  <ul class="abs dropdown"><li>Navigation 1</li><li class="current">Navigation 1</li><li>Navigation 1</li></ul>

  <!-- main slider -->
  <div class="abs slider-main">
    <div class="scene" role="img" aria-label="Featured image: a glowing pink sky over a futuristic city at dusk"></div>
    <div class="dots" style="right:14px;top:10px"><i></i><i></i><i class="on"></i><i></i></div>
    <svg class="arrow" style="left:14px;top:190px" viewBox="0 0 18 18"><path d="M12 2 5 9l7 7" fill="none" stroke="#fff" stroke-width="2.5"/></svg>
    <svg class="arrow" style="right:14px;top:190px" viewBox="0 0 18 18"><path d="m6 2 7 7-7 7" fill="none" stroke="#fff" stroke-width="2.5"/></svg>
    <div class="caption">
      <h2>Lorem Ipsum is simply dummy.</h2>
      <p>Lorem Ipsum is simply dummy text of the printing and typesetting industry. Lorem Ipsum has been the industry's standard dummy text ever since the 1500s, when an unknown printer took a galley of type and scrambled it to make a type specimen book.</p>
    </div>
  </div>

  <!-- second slider -->
  <div class="abs slider-second">
    <div class="panel">
      <h2>Here's What Photogram Ads Will Look Like</h2>
      <div class="time">3 hours ago</div>
      <p>Lorem Ipsum is simply dummy text of the printing and typesetting industry. Lorem Ipsum has been the</p>
      <div class="more">Read more</div>
    </div>
    <div class="photo" role="img" aria-label="Featured image: city lights under a violet night sky"></div>
    <div class="dots" style="right:14px;top:12px"><i></i><i></i><i class="on"></i></div>
    <svg class="arrow" style="right:40px;top:296px" viewBox="0 0 18 18"><path d="M12 2 5 9l7 7" fill="none" stroke="#fff" stroke-width="2.5"/></svg>
    <svg class="arrow" style="right:14px;top:296px" viewBox="0 0 18 18"><path d="m6 2 7 7-7 7" fill="none" stroke="#fff" stroke-width="2.5"/></svg>
  </div>

  <!-- latest news grid -->
  <h2 class="abs section-title" style="left:86px;top:968px">Latest News</h2>
  <div class="abs title-dots" style="left:740px;top:982px"><i></i><i></i><i></i><i class="on"></i></div>

  <div class="abs card" style="left:88px;top:1010px">
    <div class="thumb" role="img" aria-label="Post feature image"><div class="ribbon"><span>New</span></div></div>
    <h3><span class="post-icon"><i></i></span>What is Lorem Ipsum?</h3>
    <p>Lorem Ipsum is simply dummy text of the printing and typeset-ting industry. Lorem Ipsum has been the industry's...</p>
    <div class="meta"><span>569 Shares</span><span>3,152 Views</span><span>21 Comments</span></div>
  </div>
  <div class="abs card" style="left:260px;top:1010px">
    <div class="thumb" role="img" aria-label="Post feature image"><div class="ribbon"><span>New</span></div></div>
    <h3><span class="post-icon"><i></i></span>What is Lorem Ipsum?</h3>
    <p>Lorem Ipsum is simply dummy text of the printing and typeset-ting industry. Lorem Ipsum has been the industry's...</p>
    <div class="meta"><span>569 Shares</span><span>3,152 Views</span><span>21 Comments</span></div>
  </div>
  <div class="abs card" style="left:434px;top:1010px">
    <div class="thumb" role="img" aria-label="Post feature image"><div class="ribbon"><span>New</span></div></div>
    <h3><span class="post-icon"><i></i></span>What is Lorem Ipsum?</h3>
    <p>Lorem Ipsum is simply dummy text of the printing and typeset-ting industry. Lorem Ipsum has been the industry's...</p>
    <div class="meta"><span>569 Shares</span><span>3,152 Views</span><span>21 Comments</span></div>
  </div>
  <div class="abs card" style="left:609px;top:1010px">
    <div class="thumb" role="img" aria-label="Post feature image"><div class="ribbon"><span>New</span></div></div>
    <h3><span class="post-icon"><i></i></span>What is Lorem Ipsum?</h3>
    <p>Lorem Ipsum is simply dummy text of the printing and typeset-ting industry. Lorem Ipsum has been the industry's...</p>
    <div class="meta"><span>569 Shares</span><span>3,152 Views</span><span>21 Comments</span></div>
  </div>

  <!-- latest news two columns -->
  <h2 class="abs section-title" style="left:86px;top:1300px">Latest News</h2>
  <div class="abs col" style="left:88px;top:1350px">
    <div class="thumb" role="img" aria-label="Post feature image"><div class="ribbon"><span>New</span></div></div>
    <h3><span class="post-icon"><i></i></span>What is Lorem Ipsum?</h3>
    <p>Lorem Ipsum is simply dummy text of the printing and typeset-ting industry. Lorem Ipsum has been the industry's...</p>
    <div class="meta">
      <svg width="16" height="14" viewBox="0 0 16 14"><path d="M1 4h3v9h10V9h1.5v5.5H1zM8 1h7v6l-2-2-4 4-1.5-1.5 4-4z"/></svg><span style="margin-right:10px">569 Shares</span>
      <svg width="18" height="12" viewBox="0 0 18 12"><path d="M9 0C4.5 0 1.5 3.5 0 6c1.5 2.5 4.5 6 9 6s7.5-3.5 9-6c-1.5-2.5-4.5-6-9-6zm0 9.5A3.5 3.5 0 1 1 9 2.5a3.5 3.5 0 0 1 0 7z"/></svg><span style="margin-right:10px">3,152 Views</span>
      <svg width="14" height="13" viewBox="0 0 14 13"><path d="M7 0C3 0 0 2.4 0 5.5c0 1.7 1 3.2 2.5 4.2L2 13l3.5-2.2c.5.1 1 .2 1.5.2 4 0 7-2.4 7-5.5S11 0 7 0z"/></svg><span>21 Comments</span>
    </div>
  </div>
  <div class="abs col" style="left:432px;top:1350px">
    <div class="thumb" role="img" aria-label="Post feature image"><div class="ribbon"><span>New</span></div></div>
    <h3><span class="post-icon"><i></i></span>What is Lorem Ipsum?</h3>
    <p>Lorem Ipsum is simply dummy text of the printing and typeset-ting industry. Lorem Ipsum has been the industry's...</p>
    <div class="meta">
      <svg width="16" height="14" viewBox="0 0 16 14"><path d="M1 4h3v9h10V9h1.5v5.5H1zM8 1h7v6l-2-2-4 4-1.5-1.5 4-4z"/></svg><span style="margin-right:10px">569 Shares</span>
      <svg width="18" height="12" viewBox="0 0 18 12"><path d="M9 0C4.5 0 1.5 3.5 0 6c1.5 2.5 4.5 6 9 6s7.5-3.5 9-6c-1.5-2.5-4.5-6-9-6zm0 9.5A3.5 3.5 0 1 1 9 2.5a3.5 3.5 0 0 1 0 7z"/></svg><span style="margin-right:10px">3,152 Views</span>
      <svg width="14" height="13" viewBox="0 0 14 13"><path d="M7 0C3 0 0 2.4 0 5.5c0 1.7 1 3.2 2.5 4.2L2 13l3.5-2.2c.5.1 1 .2 1.5.2 4 0 7-2.4 7-5.5S11 0 7 0z"/></svg><span>21 Comments</span>
    </div>
  </div>

  <!-- latest news list -->
  <h2 class="abs section-title" style="left:86px;top:1878px">Latest News</h2>
  <div class="abs wide" style="left:88px;top:1921px">
    <div class="thumb" role="img" aria-label="Post feature image"><div class="ribbon"><span>NEW</span></div></div>
    <h3><span class="post-icon"><i></i></span>What is Lorem Ipsum?</h3>
    <p>Lorem Ipsum is simply dummy text of the printing and typesetting industry. Lorem Ipsum has been the industry's standard dummy text ever since the 1500s, when an unknown printer took a galley of type and scrambled it to make a type specimen book. It has survived not only five centuries, but also the leap into electronic typesetting... <a>Read more</a></p>
    <div class="meta">
      <svg width="18" height="16" viewBox="0 0 16 14"><path d="M1 4h3v9h10V9h1.5v5.5H1zM8 1h7v6l-2-2-4 4-1.5-1.5 4-4z"/></svg><span>569 Shares</span>
      <svg width="20" height="13" viewBox="0 0 18 12"><path d="M9 0C4.5 0 1.5 3.5 0 6c1.5 2.5 4.5 6 9 6s7.5-3.5 9-6c-1.5-2.5-4.5-6-9-6zm0 9.5A3.5 3.5 0 1 1 9 2.5a3.5 3.5 0 0 1 0 7z"/></svg><span>3,152 Views</span>
      <svg width="15" height="14" viewBox="0 0 14 13"><path d="M7 0C3 0 0 2.4 0 5.5c0 1.7 1 3.2 2.5 4.2L2 13l3.5-2.2c.5.1 1 .2 1.5.2 4 0 7-2.4 7-5.5S11 0 7 0z"/></svg><span>21 Comments</span>
    </div>
  </div>
  <div class="abs wide" style="left:88px;top:2352px">
    <div class="thumb" role="img" aria-label="Post feature image"><div class="ribbon"><span>NEW</span></div></div>
    <h3><span class="post-icon"><i></i></span>What is Lorem Ipsum?</h3>
    <p>Lorem Ipsum is simply dummy text of the printing and typesetting industry. Lorem Ipsum has been the industry's standard dummy text ever since the 1500s, when an unknown printer took a galley of type and scrambled it to make a type specimen book. It has survived not only five centuries, but also the leap into electronic typesetting... <a>Read more</a></p>
    <div class="meta">
      <svg width="18" height="16" viewBox="0 0 16 14"><path d="M1 4h3v9h10V9h1.5v5.5H1zM8 1h7v6l-2-2-4 4-1.5-1.5 4-4z"/></svg><span>569 Shares</span>
      <svg width="20" height="13" viewBox="0 0 18 12"><path d="M9 0C4.5 0 1.5 3.5 0 6c1.5 2.5 4.5 6 9 6s7.5-3.5 9-6c-1.5-2.5-4.5-6-9-6zm0 9.5A3.5 3.5 0 1 1 9 2.5a3.5 3.5 0 0 1 0 7z"/></svg><span>3,152 Views</span>
      <svg width="15" height="14" viewBox="0 0 14 13"><path d="M7 0C3 0 0 2.4 0 5.5c0 1.7 1 3.2 2.5 4.2L2 13l3.5-2.2c.5.1 1 .2 1.5.2 4 0 7-2.4 7-5.5S11 0 7 0z"/></svg><span>21 Comments</span>
    </div>
  </div>

  <div class="abs pager">
    <span>&#9664;&nbsp; Older</span><span style="width:40px"></span>
    <span class="num">1</span><span class="num on">2</span><span class="num">3</span><span class="num">4</span><span class="num">5</span><span class="num">6</span><span class="num">7</span>
    <span class="newer">Newer &nbsp;&#9654;</span>
  </div>

  <!-- sidebar -->
  <div class="abs widget signin">
    <h4>Sign In</h4>
    <p>Just select your favorite social network to get started</p>
    <div class="nets"><span style="background:#4a66a8"></span><span style="background:#3aa3e0"></span><span style="background:#d3473a"></span><span style="background:#2d7bb5"></span></div>
  </div>

  <div class="abs widget recent">
    <div class="widget-head"><span>Recent Post</span><span class="title-dots"><i class="on"></i><i></i><i></i></span></div>
    <ul class="postlist">
      <li><div class="sq"></div><div><b>Lorem Ipsum is simply dummy text of the printing and typesetting industry...</b><small>1 day ago</small></div></li>
      <li><div class="sq"></div><div><b>Lorem Ipsum is simply dummy text of the printing and typesetting industry...</b><small>1 day ago</small></div></li>
      <li><div class="sq"></div><div><b>Lorem Ipsum is simply dummy text of the printing and typesetting industry...</b><small>1 day ago</small></div></li>
      <li><div class="sq"></div><div><b>Lorem Ipsum is simply dummy text of the printing and typesetting industry...</b><small>1 day ago</small></div></li>
      <li><div class="sq"></div><div><b>Lorem Ipsum is simply dummy text of the printing and typesetting industry...</b><small>1 day ago</small></div></li>
    </ul>
  </div>

  <div class="abs widget newsletter">
    <h4>Join the Newsletter</h4>
    <p>Sign up for our personalized daily newsletter</p>
    <form><div class="field">Enter email address</div><div class="btn">SIGN UP</div></form>
  </div>

  <div class="abs category">
    <h4>Catagory</h4>
    <div class="tags">
      <span>Catagory 1</span><span>Catagory 1</span><span>Catagory 1</span><span>Catagory 1</span><span>Cata</span>
      <span>Cata</span><span>Catagory 1</span><span>Catagory 1</span><span>Catagory 1</span><span>Catagory</span>
      <span>Catagory 1</span><span>Cata</span><span>Catagory 1</span><span>Catagory 1</span>
      <span>Catagory 1</span><span>Catagory 1</span>
    </div>
  </div>

  <div class="abs ad side-ad">ADS</div>

  <div class="abs widget popular">
    <div class="widget-head"><span>Most popular Post</span><span class="title-dots"><i class="on"></i><i></i><i></i></span></div>
    <ul class="postlist">
      <li><div class="sq"></div><div><b>Lorem Ipsum is simply dummy text of the printing and typesetting industry...</b><small>1 day ago</small></div></li>
      <li><div class="sq"></div><div><b>Lorem Ipsum is simply dummy text of the printing and typesetting industry...</b><small>1 day ago</small></div></li>
      <li><div class="sq"></div><div><b>Lorem Ipsum is simply dummy text of the printing and typesetting industry...</b><small>1 day ago</small></div></li>
      <li><div class="sq"></div><div><b>Lorem Ipsum is simply dummy text of the printing and typesetting industry...</b><small>1 day ago</small></div></li>
      <li><div class="sq"></div><div><b>Lorem Ipsum is simply dummy text of the printing and typesetting industry...</b><small>1 day ago</small></div></li>
    </ul>
  </div>

  <!-- footer -->
  <footer class="abs footer">
    <div class="abs flogo">
      <div class="name">Logo Here</div>
      <div class="slogan">Logo Slogan Goes Here</div>
      <p>Lorem Ipsum is simply dummy text of the printing and typesetting industry. Lorem Ipsum has been the industry's standard dummy text ever since the 1500s, when an unknown printer took a galley of type and scrambled it to make a type specimen book. It has survived not only five centuries, but also the leap into electronic typesetting, remaining essentially unchanged.</p>
    </div>
    <div class="abs tweets">
      <h4 class="fcol-title">Chirper</h4>
      <ul>
        <li><span class="dot"></span><div><p>@Lorem Ipsum is simply dummy text of the printing and typesetting industry. Lorem Ipsum has been the industry's standard dummy text ever since the 1500s</p><small>3 hours ago</small></div></li>
        <li><span class="dot"></span><div><p>@Lorem Ipsum is simply dummy text of the printing and typesetting industry. Lorem Ipsum has been the industry's standard dummy text ever since the 1500s</p><small>3 hours ago</small></div></li>
        <li><span class="dot"></span><div><p>@Lorem Ipsum is simply dummy text of the printing and typesetting industry. Lorem Ipsum has been the industry's standard dummy text ever since the 1500s</p><small>3 hours ago</small></div></li>
      </ul>
    </div>
    <div class="abs calendar">
      <h4 class="fcol-title">Calender</h4>
      <div class="cal">
        <div class="month"><span>&#9664;</span><span>MARCH 2015</span><span>&#9654;</span></div>
        <table>
          <tr><th>Su</th><th>Mo</th><th>Tu</th><th>We</th><th>Th</th><th>Fr</th><th>Sa</th></tr>
          <tr><td class="o">26</td><td class="o">27</td><td class="o">28</td><td class="o">29</td><td class="o">30</td><td class="o">31</td><td>1</td></tr>
          <tr><td>2</td><td>3</td><td>4</td><td>5</td><td>6</td><td>7</td><td>8</td></tr>
          <tr><td>9</td><td>10</td><td>11</td><td>12</td><td>13</td><td>14</td><td class="today"><span>15</span></td></tr>
          <tr><td>16</td><td>17</td><td>18</td><td>19</td><td>20</td><td>21</td><td>22</td></tr>
          <tr><td>23</td><td>24</td><td>25</td><td>26</td><td>27</td><td>28</td><td>29</td></tr>
          <tr><td>30</td><td class="o">1</td><td class="o">2</td><td class="o">3</td><td class="o">4</td><td class="o">5</td><td class="o">6</td></tr>
        </table>
      </div>
    </div>
  </footer>
  <div class="abs footbar">
    <span>© Copyright 2015, All Rights Reserved</span>
    <div class="follow"><span style="background:none;width:auto;height:auto">Follow Us :</span><span></span><span></span><span></span><span></span><span></span><span></span><span></span><span></span><span></span><span></span></div>
  </div>

</div>
</body>
</html>
```